Motivationsplakat
Zielgruppe
Wir, der FC Lindmark aus der Schweiz, sind ein Fussballverein welcher in der 4. höchsten Liga spielt. Der hier zu erstellende Banner (Fusszeile) ist vorwiegend für die Spieler der 1. Mannschaft, als 'Motivationsspritze' auf diversen Plakaten (z.B. auf A1 Plakat wo die Aufstellung draufgeschrieben wird), gedacht.
Aufgabenstellung
Der Banner (als Fussleiste eines Plakates oder als eigenständiger Banner benutzbar) sollte ein Verhältniss von 1 zu 4 haben (also z.B. 50 cm hoch und 200 cm breit). Auf dem Banner muss das Logo des FC Lindmark drauf sein (im Anhang). Dazu muss es folgende Texte enthalten:
- Saison 2017/18
- Die Leidenschaft und den Verein im Herzen!
Der Spruch sollte als zentrale Botschaft verstanden werden und durch die grafische Gestalltung verstärkt/unterstützt werden.
Im Anhang sende ich ihnen noch ein paar Fotos von Spielern, welche sie eventuell verwenden könnten (muss nicht sein). Es dürften jedoch keine Spielergesichter erkennbar sein, also nur z.B. das Dress.

```html
<!DOCTYPE html>
<html lang="de">
<head>
<meta charset="utf-8">
<title>FC Lindmark – Saison 2017/18</title>
<link href="https://fonts.googleapis.com/css2?family=Bangers&family=Carlito&display=swap" rel="stylesheet">
<style>
  :root {
    --banner-bg: #d5ec6b;
    --ink: #111111;
    --club-red: #e3141d;
    --crest-white: #ffffff;
  }
  html, body {
    margin: 0;
    padding: 0;
    overflow: hidden;
    width: 1200px;
    height: 301px;
    background: var(--banner-bg);
  }
  .banner {
    position: relative;
    width: 1200px;
    height: 301px;
    background: var(--banner-bg);
    overflow: hidden;
  }
  .club-mark {
    position: absolute;
    left: 14px;
    top: 4px;
    width: 212px;
    height: 212px;
  }
  .club-mark__circle {
    position: absolute;
    inset: 0;
    border-radius: 50%;
    background: var(--crest-white);
  }
  .club-mark__name {
    position: absolute;
    left: -6px;
    right: -6px;
    top: 50%;
    transform: translateY(-50%);
    text-align: center;
    font-family: "Bangers", "Impact", sans-serif;
    font-size: 44px;
    letter-spacing: 1px;
    color: var(--club-red);
    line-height: 1;
    white-space: nowrap;
  }
  .season {
    position: absolute;
    left: 70px;
    top: 226px;
    font-family: "Carlito", "Calibri", sans-serif;
    font-size: 41px;
    color: var(--ink);
    line-height: 1;
    white-space: nowrap;
  }
  .slogan {
    position: absolute;
    left: 380px;
    top: 40px;
    width: 770px;
    margin: 0;
    text-align: center;
    font-family: "Bangers", "Impact", sans-serif;
    font-weight: 400;
    font-size: 60px;
    line-height: 106px;
    letter-spacing: 1px;
    color: var(--ink);
    text-transform: uppercase;
    white-space: nowrap;
  }
  .slogan span { display: block; }
</style>
</head>
<body>
  <div class="banner">
    <div class="club-mark">
      <div class="club-mark__circle"></div>
      <div class="club-mark__name">FC Lindmark</div>
    </div>
    <div class="season">Saison 2017/18</div>
    <h1 class="slogan">
      <span>Die Leidenschaft und den Verein</span>
      <span>im Herzen!</span>
    </h1>
  </div>
</body>
</html>
```